Business card for Autism Consultancy

I need a double-sided business card for Brightpath Learning Consultancy
Please try to use the colours and graphics in line with our website www.brightpathlearn.nz
Front side
Logo and the name of the company – Brightpath Learning Consultancy
We use Child-Centred, Modern and Innovative approaches
Teaching autistic children to bond, laugh and play
www.brightpathlearn.nz
info@brightpathlearn.nz
phone +64 09 37 615 48
Back side
Photo
Mirela Dunstan
Founder
Postgraduate Autism (Children) Specialist (with Merit)
Qualified by the Faculty of Learning Support and Access Studies (FLSA), Harwell Vale University
mirela@brightpathlearn.nz
phone +64 937 615 48
mobile: +64 20 6283 9150
Please do not convert the text fields to outlines, i.e. I need to be able to edit any text after.
The final design should be either in Adobe Illustrator or Adobe Photoshop format.
The Specs for the business card are:
Full Bleed Size
94 x 58 mm
1110 x 685 pixels
Document Trim Size
91 x 55 mm
1075 x 650 pixels

```html
<!DOCTYPE html>
<html lang="en">
<head>
<meta charset="utf-8">
<title>Brightpath Learning Consultancy – Business Card</title>
<link href="https://fonts.googleapis.com/css2?family=Germania+One&family=Nunito:wght@400;500;600&display=swap" rel="stylesheet">
<style>
  :root {
    --backdrop: #d3d3d3;
    --card: #ffffff;
    --navy: #22305a;
    --teal: #53c4be;
    --grey: #9a9a9a;
    --coral: #ef6b5b;
    --skin: #c98a68;
  }
  * { margin: 0; padding: 0; box-sizing: border-box; }
  html, body { width: 1200px; height: 1200px; overflow: hidden; }
  body {
    background: var(--backdrop);
    position: relative;
    font-family: "Nunito", sans-serif;
  }
  .card {
    position: absolute;
    top: 330px;
    width: 326px;
    height: 541px;
    background: var(--card);
    border-radius: 9px;
    overflow: hidden;
    box-shadow: 0 1px 4px rgba(0,0,0,.35);
    text-align: center;
  }
  .card--person { left: 260px; }
  .card--company { left: 614px; }

  .person-name {
    position: absolute; top: 46px; left: 0; right: 0;
    font-family: "Germania One", sans-serif;
    font-size: 35px; letter-spacing: 1.5px;
    color: var(--navy); font-weight: 400;
  }
  .portrait {
    position: absolute; left: 100px; top: 446px;
    width: 130px; height: 130px; border-radius: 50%;
    top: 116px; left: 102px;
    background: radial-gradient(circle at 55% 45%, #e0a07c 0%, var(--skin) 35%, #6b4a35 70%, #3c2b22 100%);
  }
  .role {
    position: absolute; top: 256px; left: 0; right: 0;
    font-family: "Germania One", sans-serif;
    font-size: 20px; letter-spacing: 1px; color: var(--teal);
  }
  .qualification {
    position: absolute; top: 286px; left: 0; right: 0;
    font-size: 15px; line-height: 18px; color: var(--navy); font-weight: 500;
  }
  .credential {
    position: absolute; top: 329px; left: 30px; right: 30px;
    font-size: 12.3px; line-height: 15.5px; color: var(--grey);
  }
  .contact-band {
    position: absolute; left: 0; right: 0; bottom: 0; height: 120px;
    background: var(--teal); color: #fff;
  }
  .contact-row {
    position: absolute; left: 0; right: 0;
    display: flex; align-items: center;
    font-size: 17px; font-weight: 500; letter-spacing: .3px;
  }
  .contact-row svg { position: absolute; }
  .contact-band .contact-row { color: #fff; }
  .contact-band .contact-row--email { top: 44px; }
  .contact-band .contact-row--phone { top: 69px; }
  .contact-row .text { width: 100%; }
  .contact-band .text { padding-left: 50px; }

  .brand {
    position: absolute; top: 176px; left: 22px; right: 22px;
    display: flex; align-items: center; gap: 12px; text-align: left;
  }
  .brand-dot {
    flex: 0 0 44px; height: 44px; border-radius: 50%;
    background: var(--teal);
  }
  .brand-name {
    font-size: 21px; line-height: 25px; font-weight: 600; color: var(--navy);
  }
  .card--company .contact-row { color: var(--navy); }
  .card--company .contact-row--email { top: 450px; }
  .card--company .contact-row--phone { top: 476px; }
  .card--company .text { padding-left: 42px; }
  .web-strip {
    position: absolute; left: 0; right: 0; bottom: 0; height: 10px;
    background: var(--teal);
  }
  .web-tab {
    position: absolute; left: 50px; width: 229px; bottom: 0; height: 29px;
    background: var(--teal);
    border-radius: 9px 9px 0 0;
    clip-path: polygon(3% 0, 97% 0, 100% 100%, 0 100%);
    color: #fff; font-size: 16px; font-weight: 500; letter-spacing: .4px;
    line-height: 31px;
  }
</style>
</head>
<body>

<section class="card card--person">
  <h1 class="person-name">Mirela Dunstan</h1>
  <div class="portrait" role="img" aria-label="Portrait photograph of Mirela Dunstan"></div>
  <p class="role">Founder</p>
  <p class="qualification">Postgraduate Autism (Children)<br>Specialist (with Merit)</p>
  <p class="credential">Qualified by the Faculty of Learning Support and Access Studies (FLSA), Harwell Vale University</p>
  <div class="contact-band">
    <div class="contact-row contact-row--email">
      <svg style="left:36px" width="16" height="12" viewBox="0 0 16 12" fill="none" stroke="#fff" stroke-width="1.4"><rect x="0.7" y="0.7" width="14.6" height="10.6" rx="1"/><path d="M1 1.5 8 7l7-5.5"/></svg>
      <span class="text">mirela@brightpathlearn.nz</span>
    </div>
    <div class="contact-row contact-row--phone">
      <svg style="left:38px" width="12" height="18" viewBox="0 0 12 18" fill="none" stroke="#fff" stroke-width="1.4"><rect x="0.7" y="0.7" width="10.6" height="16.6" rx="1.5"/><path d="M1 13.5h10"/><circle cx="6" cy="15.5" r=".6" fill="#fff"/></svg>
      <span class="text">+64 20 6283 9150</span>
    </div>
  </div>
</section>

<section class="card card--company">
  <div class="brand">
    <span class="brand-dot"></span>
    <span class="brand-name">Brightpath Learning Consultancy</span>
  </div>
  <div class="contact-row contact-row--email">
    <svg style="left:54px" width="16" height="12" viewBox="0 0 16 12" fill="none" stroke="#ef6b5b" stroke-width="1.3"><rect x="0.7" y="0.7" width="14.6" height="10.6" rx="1"/><path d="M1 1.5 8 7l7-5.5"/></svg>
    <span class="text">info@brightpathlearn.nz</span>
  </div>
  <div class="contact-row contact-row--phone">
    <svg style="left:54px" width="16" height="16" viewBox="0 0 16 16" fill="none" stroke="#ef6b5b" stroke-width="1.2"><path d="M3.5 1.5 6 4.5 4.7 6.2c.8 2 2.4 3.6 4.4 4.4L10.8 9.3l3 2.5-1.6 2.2C7 13.6 2.4 9 2 3.3z"/><path d="M9 3.2a4 4 0 0 1 3.8 3.8M9 .8a6.4 6.4 0 0 1 6.2 6.2"/></svg>
    <span class="text">+64 09 37 615 48</span>
  </div>
  <div class="web-strip"></div>
  <div class="web-tab">www.brightpathlearn.nz</div>
</section>

</body>
</html>
```